Dance Card to Provide Contact Info

I'm looking for a double sided business card to provide contact information to perspective dance partners.
One side of the card would have the words: "Yes I would love to Dance" written in an interesting and eye catching way. Below that would be the three categories I'm interested in
>Social >Exhibition >Competition
The other side of the card would include a picture of me with my Name, Phone Number, and Email Address (Dale Pruitt, 210-574-1328, dale@twirlnstep.dance)
My target market is middle aged women interested in Country and Western dancing and West Coast Swing dancing. I am NOT particularly interested in Ballroom style.
Here are a few links to the type of dancing I want to do:
http://www.plvkrn.org/
http://www.prairiefolkstepsociety.com/
http://mesquitevalleytwostep.com/
Dale Pruitt
210-574-1328
dale@twirlnstep.dance

```html
<!DOCTYPE html>
<html lang="en">
<head>
<meta charset="utf-8">
<title>Dale Pruitt – Dance Card</title>
<link href="https://fonts.googleapis.com/css2?family=Josefin+Sans:wght@300;700&display=swap" rel="stylesheet">
<style>
  :root{
    --page:#e4e5e7;
    --plum:#5a1f6a;
    --magenta:#a3256b;
    --crimson:#d8232e;
    --orange:#ef6a1f;
    --amber:#f6b43a;
    --cream:#fbf5e3;
    --white:#ffffff;
    --name-first:#e8571c;
    --name-last:#a11f66;
  }
  *{margin:0;padding:0;box-sizing:border-box}
  html,body{width:1200px;height:1200px;overflow:hidden}
  body{background:radial-gradient(circle at 50% 50%,#f7f7f8 0%,var(--page) 75%);position:relative;font-family:"Josefin Sans",sans-serif}

  .card{position:absolute;left:160px;width:880px;height:503px;overflow:hidden;
    box-shadow:0 14px 30px rgba(60,30,70,.28);
    background:
      linear-gradient(130deg,transparent 0 30%,rgba(255,255,255,.10) 30% 34%,transparent 34% 58%,rgba(0,0,0,.10) 58% 66%,transparent 66%),
      linear-gradient(120deg,transparent 0 18%,rgba(255,220,140,.35) 18% 21%,transparent 21% 40%,rgba(255,255,255,.08) 40% 47%,transparent 47%),
      radial-gradient(ellipse at 48% 8%,var(--amber) 0%,rgba(246,180,58,0) 38%),
      radial-gradient(ellipse at 75% 30%,var(--crimson) 0%,rgba(216,35,46,0) 55%),
      linear-gradient(170deg,var(--orange) 0%,var(--crimson) 35%,var(--magenta) 65%,var(--plum) 100%);
  }
  .card--front{top:70px}
  .card--back{top:627px}

  /* front */
  .front-frame{position:absolute;inset:20px;border:2px solid rgba(255,255,255,.85)}
  .headline{position:absolute;left:0;right:0;top:80px;text-align:center;font-weight:700;color:var(--white)}
  .headline__yes{display:block;font-size:200px;line-height:1;color:var(--cream);letter-spacing:4px}
  .headline__line{display:block;font-size:54px;line-height:1;margin-top:6px}
  .categories{position:absolute;left:0;right:0;top:395px;text-align:center;color:var(--white);font-weight:300;font-size:26px;letter-spacing:4px}

  /* back */
  .name-pill{position:absolute;left:90px;top:72px;width:480px;height:68px;border-radius:34px;background:var(--white);
    box-shadow:0 6px 10px rgba(0,0,0,.25);display:flex;align-items:center;justify-content:center;gap:22px;
    font-weight:700;font-size:44px;letter-spacing:12px;padding-top:8px}
  .name-pill__first{color:var(--name-first)}
  .name-pill__last{color:var(--name-last)}
  .portrait{position:absolute;left:96px;top:180px;width:222px;height:250px;border-radius:44px;border:4px solid var(--white);
    background:radial-gradient(ellipse at 50% 40%,#8a6a55 0%,#4a3a32 60%,#2a2220 100%);box-shadow:0 6px 12px rgba(0,0,0,.3);z-index:2}
  .contact{position:absolute;left:335px;top:168px;list-style:none;color:var(--white);font-weight:300;font-size:27px}
  .contact li{display:flex;align-items:center;gap:10px;margin-bottom:8px}
  .contact svg{width:28px;height:28px;flex:none}
  .dancers{position:absolute;left:510px;top:240px;width:340px;height:190px;border-radius:40px;
    background:radial-gradient(ellipse at 50% 60%,rgba(255,255,255,.7) 0%,rgba(255,255,255,.3) 60%,rgba(255,255,255,0) 85%)}
  .splash{position:absolute;left:0;right:0;bottom:0;height:100px;
    background:linear-gradient(to top,rgba(255,255,255,.95) 0%,rgba(255,255,255,.7) 55%,rgba(255,255,255,0) 100%)}
</style>
</head>
<body>

<section class="card card--front" aria-label="Card front">
  <div class="front-frame"></div>
  <h1 class="headline">
    <span class="headline__yes">YES</span>
    <span class="headline__line">I would love to Dance</span>
  </h1>
  <p class="categories">Social-Exhibition-Competition</p>
</section>

<section class="card card--back" aria-label="Card back">
  <div class="name-pill"><span class="name-pill__first">Dale</span><span class="name-pill__last">Pruitt</span></div>
  <ul class="contact">
    <li>
      <svg viewBox="0 0 28 28" aria-hidden="true"><circle cx="14" cy="14" r="13" fill="#fff"/><path d="M10 7c1 0 2 2.5 2 3.2s-1.4 1.3-1.2 2c.6 1.8 2.2 3.4 4 4 .7.2 1.3-1.2 2-1.2s3.2 1 3.2 2-1.6 3-3 3C11.5 20 8 16.5 8 11.5 8 9 9 7 10 7z" fill="#e8571c"/></svg>
      210-574-1328
    </li>
    <li>
      <svg viewBox="0 0 28 28" aria-hidden="true"><circle cx="14" cy="14" r="13" fill="#fff"/><text x="14" y="19.5" text-anchor="middle" font-family="Josefin Sans, sans-serif" font-weight="700" font-size="17" fill="#a11f66">@</text></svg>
      dale@twirlnstep.dance
    </li>
  </ul>
  <div class="portrait" role="img" aria-label="Portrait photo of Dale Pruitt"></div>
  <div class="dancers" role="img" aria-label="White silhouettes of country dance couples"></div>
  <div class="splash" role="img" aria-label="White paint splash border along the bottom"></div>
</section>

</body>
</html>
```